Investment Group needs a web page design

We need a web page design for a San Francisco-based investment group called 'Talvirow LLC'. The final design should be stylish and attractive to the idea while retaining a sense of stability and professionalism. A great example is http://brambleharborgroup.com/.

I am attaching the group's logo which should be the base for the webpage design.
Updates

Please note that I am interested in a single webpage that presents basic information. See the following example: http://brambleharborgroup.com/

Target Market(s)

persons doing initial due diligence and trying to assess what kind of group we are.

Industry/Entity Type

Investment

Font styles to use
Serif

Colors
86acd3
3176b5
0355a3

Requirements
Nice to have
• Would love the design to incorporate the concept - 'Sen no Sen: a block and counter attack while the opponent is attacking.'
Should not have
• Do not include trite illustrations related to finance, money or investing.

```html
<!DOCTYPE html>
<html lang="en">
<head>
<meta charset="utf-8">
<title>Talvirow LLC</title>
<link rel="stylesheet" href="https://fonts.googleapis.com/css2?family=Oswald:wght@400;500&family=Open+Sans:wght@400&family=Josefin+Sans:wght@300&display=swap">
<style>
  :root{
    --sky-top:#5d6f86;
    --sky-mid:#8a93a3;
    --horizon:#e39a4a;
    --water-top:#3d4a5e;
    --water-low:#1f2c40;
    --header-veil:rgba(205,214,226,0.55);
    --ink:#111111;
    --white:#ffffff;
    --footer:#000000;
    --footer-text:#9a9a9a;
    --footer-bright:#b8b8b8;
    --button:#3a3a3a;
  }
  *{margin:0;padding:0;box-sizing:border-box}
  html,body{width:1200px;height:726px;overflow:hidden;background:var(--footer)}
  .page{position:relative;width:1200px;height:726px;overflow:hidden}
  .hero-photo{
    position:absolute;left:0;top:0;width:1200px;height:637px;
    background:linear-gradient(180deg,var(--sky-top) 0%,var(--sky-mid) 30%,#b9a99a 44%,var(--horizon) 49%,#4d4a4c 54%,var(--water-top) 62%,#566578 78%,var(--water-low) 100%);
  }
  .header{
    position:absolute;left:0;top:0;width:1200px;height:110px;background:var(--header-veil);
  }
  .brand{position:absolute;left:172px;top:32px;display:flex;align-items:center;gap:10px}
  .brand-mark{width:42px;height:42px;background:var(--ink)}
  .brand-name{font-family:'Josefin Sans',sans-serif;font-weight:300;font-size:43px;letter-spacing:1px;color:var(--ink);line-height:1;padding-top:6px}
  .nav{position:absolute;top:40px;left:629px;display:flex;gap:27px;list-style:none}
  .nav a{font-family:'Oswald',sans-serif;font-size:18px;color:var(--ink);text-decoration:none;letter-spacing:-0.2px}
  .hero-copy{position:absolute;left:172px;top:276px;width:370px;color:var(--white)}
  .hero-title{font-family:'Oswald',sans-serif;font-weight:500;font-size:38px;letter-spacing:-0.5px;line-height:1.1;margin-bottom:16px}
  .hero-text{font-family:'Open Sans',sans-serif;font-size:13px;line-height:22px;text-align:justify}
  .read-more{display:inline-block;margin-top:18px;background:var(--button);color:var(--white);font-family:'Open Sans',sans-serif;font-size:16px;padding:7px 14px;border-radius:3px;text-decoration:none}
  .slide-arrow{position:absolute;top:363px}
  .slide-arrow.prev{left:54px}
  .slide-arrow.next{left:1078px}
  .footer{position:absolute;left:0;top:637px;width:1200px;height:89px;background:var(--footer);font-family:'Open Sans',sans-serif}
  .copyright{position:absolute;left:171px;top:22px;font-size:11.5px;color:var(--footer-text)}
  .footer-links{position:absolute;left:172px;top:50px;font-size:11.5px;color:var(--footer-text)}
  .footer-links a{color:var(--footer-text);text-decoration:none}
  .footer-links span{margin:0 7px}
  .social{position:absolute;left:520px;top:30px;display:flex;gap:5px}
  .contact{position:absolute;left:811px;top:20px;color:var(--footer-text)}
  .contact-row{display:flex;align-items:center;gap:9px}
  .contact-row.address{font-size:12px}
  .contact-row.phone{font-size:16px;margin-top:9px}
</style>
</head>
<body>
<div class="page">
  <div class="hero-photo" role="img" aria-label="City skyline at dusk beside a river with a bridge and lit towers reflected in the water"></div>

  <header class="header">
    <div class="brand">
      <div class="brand-mark"></div>
      <div class="brand-name">TALVIROW</div>
    </div>
    <ul class="nav">
      <li><a href="#">Home</a></li>
      <li><a href="#">About</a></li>
      <li><a href="#">How Does it Work?</a></li>
      <li><a href="#">Services</a></li>
      <li><a href="#">Contact Us</a></li>
    </ul>
  </header>

  <section class="hero-copy">
    <h1 class="hero-title">Welcome To Talvirow LLC</h1>
    <p class="hero-text">Lorem ipsum dolor sit amet, consectetur adipisicing elit, sed do eiusmod tempor incididunt ut labore et dolore magna aliqua. Ut enim ad minim veniam, quis nostrud exercitation ullamco laboris nisi ut aliquip ex ea commodo consequat.</p>
    <a class="read-more" href="#">Read More</a>
  </section>

  <svg class="slide-arrow prev" width="62" height="62" viewBox="0 0 62 62" aria-label="Previous slide">
    <circle cx="31" cy="31" r="29" fill="none" stroke="#e6e6e6" stroke-width="2" opacity="0.8"/>
    <polyline points="35,19 24,31 35,43" fill="none" stroke="#e6e6e6" stroke-width="2" opacity="0.8"/>
  </svg>
  <svg class="slide-arrow next" width="62" height="62" viewBox="0 0 62 62" aria-label="Next slide">
    <circle cx="31" cy="31" r="29" fill="none" stroke="#e6e6e6" stroke-width="2" opacity="0.8"/>
    <polyline points="27,19 38,31 27,43" fill="none" stroke="#e6e6e6" stroke-width="2" opacity="0.8"/>
  </svg>

  <footer class="footer">
    <p class="copyright">©2013 - 2014 &nbsp;Talvirow, All Rights Reserved.</p>
    <nav class="footer-links"><a href="#">Home</a><span>|</span><a href="#">finance</a><span>|</span><a href="#">About Us</a><span>|</span><a href="#">contact</a></nav>
    <div class="social">
      <svg width="29" height="29"><circle cx="14.5" cy="14.5" r="13.5" fill="none" stroke="#8a8a8a" stroke-width="1.5"/></svg>
      <svg width="29" height="29"><circle cx="14.5" cy="14.5" r="13.5" fill="none" stroke="#8a8a8a" stroke-width="1.5"/></svg>
      <svg width="29" height="29"><circle cx="14.5" cy="14.5" r="13.5" fill="none" stroke="#8a8a8a" stroke-width="1.5"/></svg>
      <svg width="29" height="29"><circle cx="14.5" cy="14.5" r="13.5" fill="none" stroke="#8a8a8a" stroke-width="1.5"/></svg>
      <svg width="29" height="29"><circle cx="14.5" cy="14.5" r="13.5" fill="none" stroke="#8a8a8a" stroke-width="1.5"/></svg>
    </div>
    <div class="contact">
    <div class="contact-row address">
        <svg width="12" height="17" viewBox="0 0 12 17"><path d="M6 0C2.7 0 0 2.6 0 5.9 0 10 6 17 6 17s6-7 6-11.1C12 2.6 9.3 0 6 0zm0 8.3a2.4 2.4 0 1 1 0-4.8 2.4 2.4 0 0 1 0 4.8z" fill="#a0a0a0"/></svg>
        <span>(415) 555-0148 &nbsp;Address San Francisco,</span>
      </div>
      <div class="contact-row phone">
        <svg width="16" height="16" viewBox="0 0 16 16"><path d="M1 5c0-2 3-3 7-3s7 1 7 3v1h-4V4.5H5V6H1z" fill="#a0a0a0"/><rect x="3" y="7" width="10" height="8" rx="1" fill="#a0a0a0"/><circle cx="8" cy="11" r="2" fill="#000"/></svg>
        <span>(415) 555-0148</span>
      </div>
    </div>
  </footer>
</div>
</body>
</html>
```